Make a creative business cards for our agency

We are a creative, digital marketing and IT development agency. We need a new: flat design, modern-corporate, not much elements, two sided business cards based in our logo (which I provide here in jpg and psd).

We prefer a vertical design, please no, qr codes no complex backgrounds, NO TEMPLATES.

We want to include:

Logo/Name of the agency
Slogan
Name
Title
Email
Phone
Web url
Social Media (Facebook, Twitter and Youtube)
You can simulate all this info and just place invented info.

Feel free to propose. Very important is to keep the same dark red color of the logo for a big area in the background of your design, keep the same font type preferably, you can get off of the box I you consider your idea is great.

In the case you need extra material or more brief info, just let me know please.

```html
<!DOCTYPE html>
<html lang="en">
<head>
<meta charset="utf-8">
<title>Norvale Studio — Business Cards</title>
<link rel="stylesheet" href="https://fonts.googleapis.com/css2?family=Poppins:wght@300;400&display=swap">
<style>
  :root {
    --stage: #2a2d31;
    --brand-red: #8c1116;
    --brand-red-dark: #6e0c10;
    --kraft: #b38c4e;
    --kraft-dark: #9c7740;
    --ink: #2b2116;
    --paper: #ffffff;
  }
  * { box-sizing: border-box; margin: 0; padding: 0; }
  html, body { width: 1200px; height: 900px; overflow: hidden; }
  body {
    background: var(--stage);
    font-family: "Poppins", Arial, sans-serif;
    position: relative;
  }

  /* Front: vertical card */
  .card-front {
    position: absolute;
    left: 150px; top: 150px;
    width: 360px; height: 600px;
    border-radius: 28px;
    overflow: hidden;
    background: var(--kraft);
  }
  .card-front .split {
    position: absolute; inset: 0;
    width: 100%; height: 100%;
  }
  .brand {
    position: absolute;
    left: 0; right: 0;
    display: flex; flex-direction: column; align-items: center;
    color: var(--paper);
  }
  .brand-mark {
    width: 64px; height: 64px;
    border-radius: 50%;
    background: var(--paper);
    margin-bottom: 18px;
  }
  .brand-name {
    font-weight: 300;
    font-size: 34px;
    letter-spacing: 0.5px;
    line-height: 1;
  }
  .brand-slogan {
    font-weight: 300;
    font-size: 13px;
    margin-top: 8px;
    letter-spacing: 0.3px;
  }
  .card-front .brand { top: 70px; }

  .contacts {
    position: absolute;
    left: 44px; bottom: 56px;
    list-style: none;
    color: var(--ink);
    font-size: 15px;
    font-weight: 400;
  }
  .contacts li {
    display: flex; align-items: center;
    gap: 12px;
    height: 30px;
  }
  .contacts .icon {
    width: 18px; height: 18px;
    flex: none;
  }

  /* Back: horizontal card */
  .card-back {
    position: absolute;
    left: 570px; top: 270px;
    width: 560px; height: 360px;
    border-radius: 28px;
    overflow: hidden;
    background: var(--brand-red);
  }
  .card-back::before,
  .card-back::after {
    content: "";
    position: absolute; top: 0; bottom: 0;
    width: 60px;
    background: var(--kraft);
  }
  .card-back::before { left: 0; }
  .card-back::after { right: 0; }
  .card-back .brand { top: 90px; }
</style>
</head>
<body>

  <section class="card-front" aria-label="Business card front">
    <svg class="split" viewBox="0 0 360 600" preserveAspectRatio="none" aria-hidden="true">
      <polygon points="0,0 360,0 360,290 0,375" fill="var(--brand-red)"/>
    </svg>

    <div class="brand">
      <span class="brand-mark" aria-hidden="true"></span>
      <span class="brand-name">Norvale Studio</span>
      <span class="brand-slogan">Web, Visual, IT &amp; Mkt Solutions</span>
    </div>

    <ul class="contacts">
      <li>
        <svg class="icon" viewBox="0 0 18 18" aria-hidden="true"><circle cx="9" cy="9" r="9" fill="var(--ink)"/><rect x="4" y="5.5" width="10" height="7" fill="none" stroke="var(--kraft)" stroke-width="1.2"/><polyline points="4,5.5 9,10 14,5.5" fill="none" stroke="var(--kraft)" stroke-width="1.2"/></svg>
        hello.norvale@mailbox.com
      </li>
      <li>
        <svg class="icon" viewBox="0 0 18 18" aria-hidden="true"><circle cx="9" cy="9" r="9" fill="var(--ink)"/><rect x="6.5" y="4" width="5" height="10" rx="1" fill="none" stroke="var(--kraft)" stroke-width="1.2"/></svg>
        +15550142796
      </li>
      <li>
        <svg class="icon" viewBox="0 0 18 18" aria-hidden="true"><circle cx="9" cy="9" r="9" fill="var(--ink)"/><circle cx="9" cy="9" r="5" fill="none" stroke="var(--kraft)" stroke-width="1.2"/><line x1="4" y1="9" x2="14" y2="9" stroke="var(--kraft)" stroke-width="1.2"/><ellipse cx="9" cy="9" rx="2.2" ry="5" fill="none" stroke="var(--kraft)" stroke-width="1.2"/></svg>
        www.norvalestudio.com
      </li>
      <li>
        <svg class="icon" viewBox="0 0 18 18" aria-hidden="true"><circle cx="9" cy="9" r="9" fill="var(--ink)"/></svg>
        www.clipstream.com
      </li>
      <li>
        <svg class="icon" viewBox="0 0 18 18" aria-hidden="true"><circle cx="9" cy="9" r="9" fill="var(--ink)"/></svg>
        www.friendlink.com
      </li>
      <li>
        <svg class="icon" viewBox="0 0 18 18" aria-hidden="true"><circle cx="9" cy="9" r="9" fill="var(--ink)"/></svg>
        www.chirpline.com
      </li>
    </ul>
  </section>

  <section class="card-back" aria-label="Business card back">
    <div class="brand">
      <span class="brand-mark" aria-hidden="true"></span>
      <span class="brand-name">Norvale Studio</span>
      <span class="brand-slogan">Web, Visual, IT &amp; Mkt Solutions</span>
    </div>
  </section>

</body>
</html>
```